Willowmere Loft B&B Business Card

This beautiful high-class B&B is looking for a business card that stands out from the rest. They are in the middle of the countryside, have chickens, geese and a dog. They also love bumble bees.

I was maybe thinking a rustic drawing / print of a bumble bee and a sketch of the house, I am not sure.. I quite like the feel of this... http://www.tarnwick-mill.co.uk/

Industry/Entity Type

Business

Contact Information for Business Card

Willowmere Loft
Bed & Breakfast
Brackleford, Hensworth, Somerset, TA14 7QP
01632 960418 | www.willowmereloft.co.uk

```html
<!DOCTYPE html>
<html lang="en">
<head>
<meta charset="utf-8">
<title>Willowmere Loft B&amp;B Business Card</title>
<link href="https://fonts.googleapis.com/css2?family=Open+Sans:wght@400;600&display=swap" rel="stylesheet">
<style>
  :root {
    --backdrop: #7a563d;
    --card-light: #ffffff;
    --card-dark: #3d2b1f;
    --ink: #3a2a20;
    --ink-light: #ffffff;
  }
  html, body {
    margin: 0;
    padding: 0;
    width: 1200px;
    height: 1000px;
    overflow: hidden;
    background: var(--backdrop);
    font-family: "Open Sans", sans-serif;
  }
  .canvas {
    position: relative;
    width: 1200px;
    height: 1000px;
  }
  .card {
    position: absolute;
    left: 266px;
    width: 666px;
    height: 397px;
    box-shadow: 0 6px 14px rgba(0,0,0,0.35);
  }
  .card--front { top: 74px; background: var(--card-light); color: var(--ink); }
  .card--back { top: 533px; background: var(--card-dark); color: var(--ink-light); }

  .details {
    position: absolute;
    left: 34px;
    top: 104px;
  }
  .details__name {
    margin: 0 0 36px;
    font-size: 19px;
    font-weight: 600;
    letter-spacing: 0.3px;
  }
  .details__line {
    margin: 0;
    font-size: 15px;
    line-height: 24px;
  }
  .details__service { margin-bottom: 2px; }
  .details__address { margin-bottom: 10px; }
  .contact {
    display: flex;
    align-items: center;
    gap: 8px;
    font-size: 15px;
    line-height: 24px;
  }
  .contact svg { width: 14px; height: 14px; fill: var(--ink); }

  .wordmark {
    position: absolute;
    margin: 0;
    font-weight: 600;
    font-size: 38px;
    white-space: nowrap;
  }
  .card--front .wordmark {
    left: 300px;
    top: 172px;
    color: var(--ink);
  }
  .card--back .wordmark {
    left: 0;
    right: 0;
    top: 148px;
    text-align: center;
    color: var(--ink-light);
  }
  .back__web {
    position: absolute;
    left: 0;
    right: 0;
    top: 345px;
    text-align: center;
    font-size: 15px;
  }
</style>
</head>
<body>
<main class="canvas">
  <section class="card card--front">
    <div class="details">
      <h1 class="details__name">WILLOWMERE LOFT</h1>
      <p class="details__line details__service">Bed &amp; Breakfast</p>
      <p class="details__line details__address">Brackleford, Hensworth,<br>Somerset, TA14 7QP</p>
      <div class="contact">
        <svg viewBox="0 0 14 14" aria-hidden="true"><path d="M1 5c0-2 3-3 6-3s6 1 6 3l-1 1.5-2.5-.7V4.5H4.5v1.3L2 6.5zM3 7.5h8l1.5 4.5h-11z"/></svg>
        <span>01632 960418</span>
      </div>
      <div class="contact">
        <svg viewBox="0 0 14 14" aria-hidden="true"><path d="M1 3.5h12v7H1zM1.8 4.3 7 8l5.2-3.7v.9L7 9 1.8 5.2z" fill-rule="evenodd"/></svg>
        <span>www.willowmereloft.co.uk</span>
      </div>
    </div>
    <p class="wordmark">Willowmere Loft</p>
  </section>

  <section class="card card--back">
    <p class="wordmark">Willowmere Loft</p>
    <p class="back__web">www.willowmereloft.co.uk</p>
  </section>
</main>
</body>
</html>
```